Birch Power and Wiring is a new company that specializes in solar pv. I need a card with similar attributes to the ones I have attached. I am after a two sided card with the logo on one side and the logo plus info on the other. I would prefer one side to be black and the other to be a colour but am open to suggestions. The colour scheme I was thinking of was blue or green. I plan on spot glossing the logos if that makes any difference. I have attached a file of my logo in a few colours, none of which I am completely sold on so please feel free to change colous to suit.
Thanks.
Calvin Birch, www.bpw.net.nz, calvin@bpw.net.nz, t. 0508 4 POWER m. 027463918

```html
<!DOCTYPE html>
<html lang="en">
<head>
<meta charset="utf-8">
<title>Birch Power and Wiring – Business Card</title>
<link rel="stylesheet" href="https://fonts.googleapis.com/css2?family=Lato:wght@300;400;700&display=swap">
<style>
  :root {
    --page: #ecebe8;
    --card-white: #ffffff;
    --brand-blue: #1d80c3;
    --panel-blue: #4b93d1;
    --ink: #2b2b2b;
    --ink-soft: #555555;
    --rule: #333333;
    --label-blue: #2f7fc4;
  }
  * { margin: 0; padding: 0; box-sizing: border-box; }
  html, body { width: 1200px; height: 2551px; overflow: hidden; }
  body {
    background: var(--page);
    font-family: "Lato", sans-serif;
    position: relative;
  }
  .card {
    position: absolute;
    left: 100px;
    width: 1000px;
    height: 572px;
    box-shadow: 0 6px 24px rgba(0,0,0,0.12);
  }
  .card--front { top: 620px; background: var(--card-white); }
  .card--back  { top: 1400px; background: var(--brand-blue); }

  .logo-panel {
    position: absolute;
    left: 150px; top: 34px;
    width: 520px; height: 190px;
    background: var(--panel-blue);
    display: flex; align-items: center; justify-content: center;
  }
  .brand-name {
    color: #ffffff;
    font-weight: 700;
    font-size: 40px;
    letter-spacing: 1px;
    text-align: center;
    line-height: 1.15;
  }
  .brand-name--large { font-size: 62px; }

  .holder-name {
    position: absolute;
    left: 40px; top: 282px;
    font-size: 74px;
    font-weight: 300;
    color: var(--ink-soft);
    line-height: 1;
  }
  .holder-name strong { font-weight: 400; color: var(--ink); }

  .company-tag {
    position: absolute;
    right: 44px; top: 318px;
    font-size: 19px;
    color: var(--label-blue);
    letter-spacing: 0.5px;
    text-transform: uppercase;
  }
  .rule {
    position: absolute;
    left: 40px; right: 44px; top: 378px;
    height: 8px;
    background: var(--rule);
  }
  .details {
    position: absolute;
    left: 40px; right: 44px; top: 412px;
    font-size: 19px;
    color: var(--ink);
    line-height: 1.6;
  }
  .details .label { color: var(--label-blue); font-weight: 700; }
  .details-row { display: flex; justify-content: space-between; align-items: baseline; }
  .details-row .item--email { margin-left: 170px; }

  .back-logo {
    position: absolute; inset: 0;
    display: flex; align-items: center; justify-content: center;
  }
</style>
</head>
<body>
  <section class="card card--front" aria-label="Card front">
    <div class="logo-panel">
      <span class="brand-name">Birch Power and Wiring</span>
    </div>
    <h1 class="holder-name">Calvin <strong>Birch</strong></h1>
    <p class="company-tag">Birch Power and Wiring</p>
    <div class="rule"></div>
    <div class="details">
      <div class="details-row">
        <span><span class="label">Address:</span> 212 Kestrel Road, 12th floor, NY USA</span>
      </div>
      <div class="details-row">
        <span><span class="label">Phone:</span> 000 . 0274 . 63918</span>
        <span class="item--email"><span class="label">Email:</span> calvin@bpw.net.nz</span>
        <span><span class="label">Website:</span> www.bpw.net.nz</span>
      </div>
    </div>
  </section>

  <section class="card card--back" aria-label="Card back">
    <div class="back-logo">
      <span class="brand-name brand-name--large">Birch Power and Wiring</span>
    </div>
  </section>
</body>
</html>
```